Powerpoint template

I am looking for a brand based PPT template that can also be used as the basis for datasheet creation. I have attached a document with some of our branding structure in as an FYI to help.

To be clear I am looking a background design, bullets, layouts, different styles for differing content types. This is a template to be used for lots of presentations.

Reason: I have committed to the payment and wanted to give people chance to respond.

Target Market(s)

Enterprise

Requirements
Must have
• Brand standard. different page design choices for different content types
Nice to have
• brand font if it works. Use of some play on the logo in bullets
Should not have
• must be on brand and focused on the business audience

```html
<!DOCTYPE html>
<html lang="en">
<head>
<meta charset="utf-8">
<title>vectorline presentation template</title>
<link href="https://fonts.googleapis.com/css2?family=Ubuntu:wght@400;500;700&family=Open+Sans:wght@400;700&display=swap" rel="stylesheet">
<style>
:root{
  --canvas:#4b525a;
  --blue:#0ba3d9;
  --green:#8bc441;
  --navy:#2a3445;
  --navy-row:#334055;
  --paper:#eef2f7;
  --ink:#3b4350;
  --muted:#5d6673;
  --red:#e9606a;
  --orange:#ee9b11;
  --line:#d3dbe4;
  --white:#ffffff;
}
*{box-sizing:border-box;margin:0;padding:0}
html,body{width:1064px;height:1200px;overflow:hidden;background:var(--canvas)}
body{position:relative;font-family:"Open Sans",sans-serif;color:var(--ink)}
.slide{position:absolute;width:582px;height:436px;transform-origin:0 0;transform:scale(.8866);overflow:hidden;background:var(--paper)}
.s1{left:12px;top:9px}.s2{left:536px;top:9px}
.s3{left:12px;top:407px}.s4{left:536px;top:407px}
.s5{left:12px;top:805px}.s6{left:536px;top:805px}
.title-band{position:absolute;left:0;top:0;width:100%;height:41px;padding-left:7px;font-family:"Ubuntu",sans-serif;font-size:27px;line-height:41px;color:var(--white)}
.band-blue{background:var(--blue)}.band-green{background:var(--green)}
.footer{position:absolute;left:0;bottom:0;width:100%;height:32px;background:var(--navy);display:flex;align-items:center;padding:0 12px}
.brand{display:flex;align-items:center;gap:4px;font-family:"Ubuntu",sans-serif;font-size:14px;color:var(--blue)}
.brand-dot{width:10px;height:10px;border-radius:50%;background:var(--blue)}
.footer-note{font-family:"Ubuntu",sans-serif;font-size:9px;color:var(--white);margin-left:8px}
.footer-note b{font-weight:700}
.footer-web{margin-left:auto;font-size:9px;color:var(--blue)}
.footer-page{margin-left:12px;font-size:9px;color:var(--green)}
/* tables */
.table-block{position:absolute;top:70px;width:260px}
.table-title{font-family:"Ubuntu",sans-serif;font-size:17px;font-weight:500;color:var(--ink);display:flex;align-items:center;gap:6px;margin-bottom:10px}
.table-title span{font-weight:400}
.tbl-icon{width:16px;height:12px;border:2px solid var(--green);background:linear-gradient(var(--green),var(--green)) 50% 50%/100% 2px no-repeat,linear-gradient(var(--green),var(--green)) 50% 50%/2px 100% no-repeat}
.data-table{width:260px;border-collapse:collapse;font-size:6.2px;text-align:center}
.data-table th{background:var(--green);color:var(--white);height:23px;font-size:8px;font-weight:700}
.data-table td{height:25.3px;border-bottom:1px solid var(--line);border-right:1px solid var(--line);line-height:1.2}
.data-table td.num{font-size:10px;color:var(--blue);width:32px}
.data-table td.step{width:100px}
.data-table td.resp{width:66px}
.light td{background:var(--white);color:var(--ink)}
.dark td{background:var(--navy-row);color:#7d8aa0;border-color:#3f4c62}
.dark td.num{background:var(--blue);color:var(--white);border-color:#1a94c4}
.table-foot{height:26px;line-height:26px;text-align:center;font-size:10px;color:var(--white)}
.light-foot{background:var(--blue)}.dark-foot{background:var(--navy)}
/* image slides */
.placeholder{position:absolute}
.drag-note{position:absolute;left:36px;top:112px;width:180px;font-family:"Ubuntu",sans-serif;font-size:13px;line-height:17px;color:var(--blue)}
.arrow-icon{position:absolute;left:227px;top:112px}
.body-copy{position:absolute;left:36px;width:218px;font-size:9.2px;line-height:12px;text-align:justify;color:var(--ink)}
.body-copy b{font-weight:700}
.bullets{position:absolute;list-style:none}
.bullets li{position:relative;padding-left:12px;font-size:8.6px;line-height:11px;color:var(--muted);margin-bottom:13px}
.bullets li::before{content:"";position:absolute;left:1px;top:1px;width:5px;height:5px;border-top:2px solid var(--green);border-right:2px solid var(--green);transform:rotate(45deg)}
.bullets.blue li::before{border-color:var(--blue)}
.bullets li b{color:var(--ink)}
/* graphs */
.graph-title{position:absolute;top:64px;font-family:"Ubuntu",sans-serif;font-size:17px;color:var(--ink)}
.graph-title b{font-weight:700}
.chart{position:absolute;left:0;top:0}
.chart text{font-family:"Open Sans",sans-serif}
/* contact */
.contact{background:var(--navy)}
.contact.alt{background:var(--blue)}
.contact-brand{position:absolute;left:0;width:100%;top:118px;display:flex;justify-content:center;align-items:center;gap:10px;font-family:"Ubuntu",sans-serif;font-size:44px;color:var(--blue)}
.contact.alt .contact-brand{color:var(--white)}
.brand-mark{width:40px;height:40px;border-radius:50%;background:var(--blue)}
.contact.alt .brand-mark{background:var(--white)}
.contact-head{position:absolute;left:0;width:100%;top:212px;text-align:center;font-family:"Ubuntu",sans-serif;font-size:48px;font-weight:500;color:var(--white)}
.office{position:absolute;top:366px;font-family:"Ubuntu",sans-serif;font-size:10px;line-height:12px;color:var(--white)}
.office h3{font-size:13px;font-weight:500;color:var(--blue);line-height:14px}
.contact.alt .office h3{color:var(--green)}
.social{position:absolute;right:14px;bottom:12px;display:flex;gap:9px;align-items:center}
.social .chip{width:11px;height:11px;border-radius:50%;background:var(--blue)}
.contact.alt .social .chip{background:var(--white)}
</style>
</head>
<body>

<!-- Slide 7: tables -->
<section class="slide s1">
  <div class="title-band band-blue">Color Style Tables</div>
  <div class="table-block" style="left:22px">
    <div class="table-title"><i class="tbl-icon"></i>Light <span>Theme</span></div>
    <table class="data-table light">
      <tr><th>Item</th><th>Step/Action</th><th>Responsible</th><th>Target Date</th></tr>
      <tr><td class="num">1</td><td class="step">Business X, Y, Z high level needs</td><td class="resp">Business X, Y, Z</td><td>5/24/2013</td></tr>
      <tr><td class="num">2</td><td class="step">Understand current situation and safety mana</td><td class="resp">Business X, Y, Z</td><td>5/31/2013</td></tr>
      <tr><td class="num">3</td><td class="step">Submit Proposal</td><td class="resp">Business X, Y, Z</td><td>6/3/2013</td></tr>
      <tr><td class="num">4</td><td class="step">Review Proposal</td><td class="resp">Business X, Y, Z</td><td>TBD</td></tr>
      <tr><td class="num">5</td><td class="step">Prepare Final Proposal &amp; Statement of Work (SOW)</td><td class="resp">Business X, Y, Z</td><td>TBD</td></tr>
      <tr><td class="num">6</td><td class="step">Complete and sign SOW</td><td class="resp">Business X, Y, Z</td><td>TBD</td></tr>
      <tr><td class="num">7</td><td class="step">Schedule project start date</td><td class="resp">Business X, Y, Z</td><td>TBD</td></tr>
      <tr><td class="num">8</td><td class="step">Kick-off Project</td><td class="resp">Business X, Y, Z</td><td>TBD</td></tr>
      <tr><td class="num">9</td><td class="step">Complete Project</td><td class="resp">Business X, Y, Z</td><td>TBD</td></tr>
    </table>
    <div class="table-foot light-foot">* Additional Information</div>
  </div>
  <div class="table-block" style="left:302px">
    <div class="table-title"><i class="tbl-icon"></i>Dark <span>Theme</span></div>
    <table class="data-table dark">
      <tr><th>Item</th><th>Step/Action</th><th>Responsible</th><th>Target Date</th></tr>
      <tr><td class="num">1</td><td class="step">Business X, Y, Z high level needs</td><td class="resp">Business X, Y, Z</td><td>5/24/2013</td></tr>
      <tr><td class="num">2</td><td class="step">Understand current situation and safety mana</td><td class="resp">Business X, Y, Z</td><td>5/31/2013</td></tr>
      <tr><td class="num">3</td><td class="step">Submit Proposal</td><td class="resp">Business X, Y, Z</td><td>6/3/2013</td></tr>
      <tr><td class="num">4</td><td class="step">Review Proposal</td><td class="resp">Business X, Y, Z</td><td>TBD</td></tr>
      <tr><td class="num">5</td><td class="step">Prepare Final Proposal &amp; Statement of Work (SOW)</td><td class="resp">Business X, Y, Z</td><td>TBD</td></tr>
      <tr><td class="num">6</td><td class="step">Complete and sign SOW</td><td class="resp">Business X, Y, Z</td><td>TBD</td></tr>
      <tr><td class="num">7</td><td class="step">Schedule project start date</td><td class="resp">Business X, Y, Z</td><td>TBD</td></tr>
      <tr><td class="num">8</td><td class="step">Kick-off Project</td><td class="resp">Business X, Y, Z</td><td>TBD</td></tr>
      <tr><td class="num">9</td><td class="step">Complete Project</td><td class="resp">Business X, Y, Z</td><td>TBD</td></tr>
    </table>
    <div class="table-foot dark-foot">* Additional Information</div>
  </div>
  <div class="footer"><span class="brand"><i class="brand-dot"></i>vectorline</span><span class="footer-note">| Company Presentation to <b>Business</b>/Client</span><span class="footer-web">www.vectorline.com</span><span class="footer-page">7</span></div>
</section>

<!-- Slide 8: portrait image -->
<section class="slide s2">
  <div class="title-band band-blue">Image in Portrait view</div>
  <div class="drag-note">Drag &amp; Drop images here It's an Image Placeholder</div>
  <svg class="arrow-icon" width="26" height="26" viewBox="0 0 26 26"><circle cx="13" cy="13" r="11.5" fill="none" stroke="#0ba3d9" stroke-width="1.6"/><path d="M7 13h11M14 9l4 4-4 4" fill="none" stroke="#0ba3d9" stroke-width="1.6"/></svg>
  <p class="body-copy" style="top:164px"><b>Lorem</b> ipsum dolor sit amet, consectetur adipiscing elit. Vivamus eget elit eu velit vehicula feugiat. Integer viverra metus vitae lacus dictum eleifend. Lorem ipsum dolor sit amet. Donec viverra lobortis feugiat. Sed id odio ante.</p>
  <p class="body-copy" style="top:248px"><b>Lorem</b> ipsum dolor sit amet, consectetur adipiscing elit. Vivamus eget elit eu velit vehicula feugiat. Integer viverra metus vitae lacus dictum eleifend. Lorem ipsum dolor sit amet. Donec viverra lobortis feugiat. Sed id odio ante.</p>
  <div class="placeholder" role="img" aria-label="Portrait image placeholder" style="left:301px;top:73px;width:247px;height:311px;background:var(--blue)"></div>
  <div class="footer"><span class="brand"><i class="brand-dot"></i>vectorline</span><span class="footer-note">| Company Presentation to <b>Business</b>/Client</span><span class="footer-web">www.vectorline.com</span><span class="footer-page">8</span></div>
</section>

<!-- Slide 9: landscape image -->
<section class="slide s3">
  <div class="title-band band-green">Image in Landscape view</div>
  <div class="placeholder" role="img" aria-label="Landscape image placeholder" style="left:38px;top:77px;width:505px;height:225px;background:var(--green)"></div>
  <ul class="bullets" style="left:42px;top:319px;width:500px">
    <li><b>Aenean</b> ridiculus tortor quis interdum id habitant ad, natoque consectetuer nisl auctor libero quisque euismod ante inceptos malesuada ligula mattis.</li>
    <li><b>Aenean</b> ridiculus tortor quis interdum id habitant ad, natoque consectetuer nisl auctor libero quisque euismod ante inceptos malesuada ligula mattis.</li>
  </ul>
  <div class="footer"><span class="brand"><i class="brand-dot"></i>vectorline</span><span class="footer-note">| Company Presentation to <b>Business</b>/Client</span><span class="footer-web">www.vectorline.com</span><span class="footer-page">9</span></div>
</section>

<!-- Slide 10: graphs -->
<section class="slide s4">
  <div class="title-band band-green">Color style graphs</div>
  <div class="graph-title" style="left:28px"><b>Graph</b> Main Colors</div>
  <div class="graph-title" style="left:331px"><b>Graph</b> Secondary Colors</div>
  <svg class="chart" width="582" height="300" viewBox="0 0 582 300">
    <g stroke="#d3dbe4" stroke-width="1">
      <line x1="48" y1="108" x2="263" y2="108"/><line x1="48" y1="149" x2="263" y2="149"/>
      <line x1="48" y1="191" x2="263" y2="191"/><line x1="48" y1="233" x2="263" y2="233"/>
    </g>
    <polygon points="48,182 120,202 192,157 215,165 263,140 263,274 48,274" fill="#8bc441"/>
    <polygon points="48,228 80,235 48,246" fill="#2a3445"/>
    <polygon points="48,246 120,230 192,185 263,113 263,274 48,274" fill="#0ba3d9"/>
    <line x1="48" y1="274" x2="263" y2="274" stroke="#2a3445" stroke-width="1"/>
    <g font-size="8" fill="#2a3445" text-anchor="end">
      <text x="40" y="111">100</text><text x="40" y="152">75</text><text x="40" y="194">50</text><text x="40" y="236">25</text><text x="40" y="277">0</text>
    </g>
    <g font-size="8" fill="#2a3445" text-anchor="middle">
      <text x="48" y="287">2007</text><text x="120" y="287">2008</text><text x="192" y="287">2009</text><text x="263" y="287">2010</text>
    </g>
    <g transform="translate(418 188)">
      <path d="M0 0L-49.8 80.9A95 95 0 0 1 44.6 -83.9Z" fill="#e9606a"/>
      <path d="M0 0L88.8 33.7A95 95 0 0 1 -49.8 80.9Z" fill="#0ba3d9"/>
      <path d="M0 0L82.7 -46.9A95 95 0 0 1 88.8 33.7Z" fill="#ee9b11"/>
      <path d="M7 -7L51.6 -90.9A95 95 0 0 1 89.7 -53.9Z" fill="#8bc441"/>
      <g font-size="11" fill="#ffffff" text-anchor="middle">
        <text x="-42" y="-18">50%</text><text x="56" y="-48">9%</text><text x="62" y="4">14%</text><text x="20" y="66">28%</text>
      </g>
    </g>
    <g font-size="7" fill="#2a3445">
      <circle cx="521" cy="240" r="3.5" fill="#8bc441"/><text x="528" y="243">2007</text>
      <circle cx="521" cy="249" r="3.5" fill="#ee9b11"/><text x="528" y="252">2008</text>
      <circle cx="521" cy="258" r="3.5" fill="#0ba3d9"/><text x="528" y="261">2009</text>
      <circle cx="521" cy="267" r="3.5" fill="#e9606a"/><text x="528" y="270">2010</text>
    </g>
  </svg>
  <ul class="bullets blue" style="left:38px;top:304px;width:230px">
    <li style="font-size:7.8px;line-height:10.5px"><b>Aenean</b> ridiculus tortor quis interdum id habitant ad, natoque consectetuer nisl auctor libero quisque euismod ante inceptos malesuada ligula mattis.</li>
    <li style="font-size:7.8px;line-height:10.5px">Varius inceptos <b>nascetur</b> mollis dui aptent ultrices. Pretium pulvinar ante lobortis convallis lectus netus vitae penatibus eros at blandit. Parturient.</li>
  </ul>
  <ul class="bullets blue" style="left:323px;top:304px;width:230px">
    <li style="font-size:7.8px;line-height:10.5px"><b>Aenean</b> ridiculus tortor quis interdum id habitant ad, natoque consectetuer nisl auctor libero quisque euismod ante inceptos malesuada ligula mattis.</li>
    <li style="font-size:7.8px;line-height:10.5px">Varius inceptos <b>nascetur</b> mollis dui aptent ultrices. Pretium pulvinar ante lobortis convallis lectus netus vitae penatibus eros at blandit. Parturient.</li>
  </ul>
  <div class="footer"><span class="brand"><i class="brand-dot"></i>vectorline</span><span class="footer-note">| Company Presentation to <b>Business</b>/Client</span><span class="footer-web">www.vectorline.com</span><span class="footer-page">10</span></div>
</section>

<!-- Contact, dark -->
<section class="slide s5 contact">
  <div class="contact-brand"><i class="brand-mark"></i>vectorline</div>
  <h2 class="contact-head">Contact Us Today!</h2>
  <div class="office" style="left:12px"><h3>Canada</h3>288 Harbour Road, Suite 900<br>Toronto, ON M4K 1B2<br>Phone: +1 416 555 0142<br>Fax: +1 416 555 0187</div>
  <div class="office" style="left:163px"><h3>USA</h3>75 Elm Court, Suite 210<br>Riverside, New York 11500<br>Phone 1: +1 516 555 0123<br>Phone 2: +1 516 555 0168</div>
  <div class="social">
    <svg width="13" height="10" viewBox="0 0 13 10"><rect x=".5" y=".5" width="12" height="9" fill="#0ba3d9"/><path d="M1 1l5.5 4.5L12 1" fill="none" stroke="#2a3445" stroke-width="1.2"/></svg>
    <i class="chip"></i><i class="chip"></i><i class="chip"></i>
  </div>
</section>

<!-- Contact, blue -->
<section class="slide s6 contact alt">
  <div class="contact-brand"><i class="brand-mark"></i>vectorline</div>
  <h2 class="contact-head">Contact Us Today!</h2>
  <div class="office" style="left:12px"><h3>Canada</h3>288 Harbour Road, Suite 900<br>Toronto, ON M4K 1B2<br>Phone: +1 416 555 0142<br>Fax: +1 416 555 0187</div>
  <div class="office" style="left:163px"><h3>USA</h3>75 Elm Court, Suite 210<br>Riverside, New York 11500<br>Phone 1: +1 516 555 0123<br>Phone 2: +1 516 555 0168</div>
  <div class="social">
    <svg width="13" height="10" viewBox="0 0 13 10"><rect x=".5" y=".5" width="12" height="9" fill="#ffffff"/><path d="M1 1l5.5 4.5L12 1" fill="none" stroke="#0ba3d9" stroke-width="1.2"/></svg>
    <i class="chip"></i><i class="chip"></i><i class="chip"></i>
  </div>
</section>

</body>
</html>
```